Trifold flyer for our dental clinic (the Bright Harbor Clinic)

The goal of this project is to design a trifold flyer for our dental clinic (the Bright Harbor Clinic). The winning design is expected to be creative, artistic and coherent with our logo.
Updates

Designs look the same

Target Market(s)

Young generation with dental need.

Industry/Entity Type

Dental Clinic

Font styles to use
Sans Serif

Colors
0355a3
85acd3
85cae6
0592cd
00a990
86cfc6
cedeed
cee9f5
cfeae6

Requirements
Must have
• See the attached sketch for content arrangement.

```html
<!DOCTYPE html>
<html lang="en">
<head>
<meta charset="utf-8">
<title>Bright Harbor Clinic – Trifold Flyer</title>
<link href="https://fonts.googleapis.com/css2?family=Montserrat:wght@400;500;600;700&display=swap" rel="stylesheet">
<style>
  :root{
    --blue:#2aa3da;
    --blue-light:#85cae6;
    --blue-pale:#cee9f5;
    --ink:#333a40;
    --grey:#6d6e70;
    --paper:#ffffff;
    --bg:#e4e4e4;
  }
  *{margin:0;padding:0;box-sizing:border-box}
  html,body{width:707px;height:1200px;overflow:hidden;background:var(--bg);font-family:"Montserrat",Arial,sans-serif;color:var(--ink)}
  .spread{position:absolute;left:10px;width:687px;height:570px;display:flex;box-shadow:0 2px 8px rgba(0,0,0,.12)}
  .spread--inside{top:20px}
  .spread--outside{top:610px}
  .panel{position:relative;width:229px;height:570px;background:var(--paper);overflow:hidden}
  .panel--shaded{background:linear-gradient(90deg,#f1f1f1,#fff 40%,#fff 70%,#f3f3f3)}
  .panel svg.band{position:absolute;left:0;width:229px}
  .band--top{top:0}
  .band--bottom{bottom:0}
  .content{position:absolute;left:18px;right:16px}
  .heading{color:var(--blue);font-weight:700;font-size:15px;letter-spacing:.5px;text-transform:uppercase}
  .promo-list p{font-size:10.5px;font-weight:500;line-height:1.3;margin-bottom:7px}
  .service-list li{list-style:none;font-size:11px;font-weight:700;text-transform:uppercase;margin-bottom:4px;letter-spacing:.3px}
  .welcome{font-size:7.2px;font-weight:600;line-height:1.35;text-align:justify}
  .pill{display:block;background:var(--blue);color:#fff;border-radius:20px;text-align:center;font-weight:600}
  .pill--small{font-size:9.5px;padding:5px 8px;margin-bottom:12px}
  .pill--hours{font-size:10.5px;font-weight:700;text-transform:uppercase;padding:8px 6px;line-height:1.2;margin-bottom:14px}
  .insured{color:var(--blue);font-size:15px;font-weight:600;text-align:center;line-height:1.2;margin:16px 0 18px}
  .no-ins{font-size:15px;font-weight:700;text-align:center;text-transform:uppercase}
  .plan-note{color:var(--blue);font-size:8.5px;font-weight:600;text-align:center;text-transform:uppercase;margin:4px 0 22px}
  .plan-row{display:flex;align-items:center;margin-bottom:22px}
  .plan-row .items{width:82px;font-size:12.5px;font-weight:500;line-height:1.3;color:var(--ink)}
  .plan-row .bracket{width:10px;align-self:stretch;border:3px solid var(--blue);border-left:none;margin-right:10px}
  .plan-row .range{font-size:11.5px;font-weight:500}
  .sat{color:var(--blue);font-size:10px;font-weight:600;text-align:center;text-transform:uppercase}
  .sat strong{display:block;font-size:17px;font-weight:700}
  .call-today{font-size:16px;font-weight:600;text-transform:uppercase;margin:14px 0 8px}
  .contact{list-style:none}
  .contact li{display:flex;align-items:flex-start;gap:7px;color:var(--blue);font-size:10px;font-weight:600;margin-bottom:7px;line-height:1.25}
  .contact svg{flex:none;width:13px;height:13px;margin-top:1px}
  .meet-title{font-size:17px;font-weight:700;text-transform:uppercase}
  .doctor{position:absolute;left:16px;right:12px}
  .doctor h3{color:var(--blue);font-size:9.5px;font-weight:600;text-transform:uppercase;margin-bottom:3px}
  .doctor .bio-row{display:flex;gap:6px;align-items:center}
  .doctor p{font-size:5.8px;line-height:1.4;flex:1}
  .portrait{flex:none;width:56px;height:56px;border-radius:50%;background:radial-gradient(circle at 50% 40%,#c9a48c,#4a3a33)}
  .reviews-title{position:absolute;top:40px;width:100%;text-align:center;color:var(--blue);font-size:16px;font-weight:700;letter-spacing:.5px}
  .cover-top{position:absolute;top:24px;left:0;right:0;text-align:center}
  .cover-top .call{color:var(--blue);font-size:15px;font-weight:700;text-transform:uppercase}
  .cover-top .phone{font-size:11px;font-weight:500}
  .brand{display:inline-flex;align-items:center;gap:6px;margin-top:6px;color:var(--blue);font-size:9.5px;font-weight:600;text-transform:uppercase;line-height:1.05;text-align:left}
  .brand .mark{width:14px;height:14px;background:var(--blue)}
  .cover-photo{position:absolute;top:100px;left:-20px;width:269px;height:270px}
  .offers{position:absolute;left:0;right:0;bottom:40px;text-align:center;color:#fff;font-weight:700;line-height:1.35}
  .offers h2{font-size:13.5px;text-transform:uppercase;margin-bottom:4px}
  .offers p{font-size:10.5px}
</style>
</head>
<body>

<!-- Inside spread -->
<section class="spread spread--inside">
  <div class="panel">
    <svg class="band band--top" viewBox="0 0 229 70" height="70">
      <path d="M0 0H229V32Q110 28 0 56Z" fill="var(--blue)"/>
      <path d="M0 62Q110 36 229 36Q110 42 0 66Z" fill="var(--blue-light)"/>
    </svg>
    <div class="content" style="top:82px">
      <h2 class="heading" style="text-align:center;margin-bottom:10px">Our Promos</h2>
      <div class="promo-list">
        <p>$69 New Patients special exam, Digital X ray. Regular price $500</p>
        <p>$99 teeth whitening regular price $700</p>
        <p>25-40% off</p>
        <p>Plus free consulation</p>
      </div>
      <h2 class="heading" style="text-align:center;margin:14px 0 10px;font-size:16px">Our Services</h2>
      <ul class="service-list">
        <li>Cleaning &amp; Presentation</li>
        <li>Cosmetic</li>
        <li>Remotable</li>
        <li>Orthopetic</li>
      </ul>
      <p class="welcome" style="margin-top:12px">Welcome to the Bright Harbor Clinic where we specialize in General and Cosmetic Dentistry, Dental Implants, Periodontics (Gum Surgery), Endodontics (Root Canal Treatment) and Reconstructive Dentistry for patients in Easton, Millbrook, Westfield and all other surrounding neighborhoods.</p>
    </div>
  </div>

  <div class="panel panel--shaded">
    <svg class="band band--top" viewBox="0 0 229 70" height="70">
      <path d="M0 0H229V36Q110 18 0 40Z" fill="var(--blue)"/>
      <path d="M40 30Q140 20 229 40Q140 26 40 30Z" fill="var(--blue-light)"/>
    </svg>
    <div class="content" style="top:60px">
      <span class="pill pill--small">Payment options available!</span>
      <span class="pill pill--small">Financial options available!</span>
      <p class="insured">Most imburances<br>accepted!</p>
      <p class="no-ins">No insurance?</p>
      <p class="plan-note">Try our denta sauzngs plan:</p>
      <div class="plan-row">
        <div class="items">Preventive<br>Exam<br>X-ray</div>
        <span class="bracket"></span>
        <span class="range">80%-100%</span>
      </div>
      <div class="plan-row">
        <div class="items">Filling<br>crowns</div>
        <span class="bracket"></span>
        <span class="range">40%-80%</span>
      </div>
    </div>
  </div>

  <div class="panel">
    <svg class="band band--top" viewBox="0 0 229 70" height="70">
      <path d="M0 0H229V22Q100 20 0 60Z" fill="var(--blue)"/>
      <path d="M0 66Q90 28 200 30Q90 34 0 70Z" fill="var(--blue-light)"/>
    </svg>
    <div class="content" style="top:78px">
      <p class="sat">Convenient Saturday<strong>Hours!</strong></p>
      <div style="margin-top:14px">
        <span class="pill pill--hours">Tuesday, Thursday<br>9:30AM-5:00PM</span>
        <span class="pill pill--hours">Friday, Saturday<br>9:00AM-5:00PM</span>
      </div>
      <p class="call-today">Call us today</p>
      <ul class="contact">
        <li><svg viewBox="0 0 24 24"><path d="M6.6 10.8a15 15 0 006.6 6.6l2.2-2.2a1 1 0 011-.25 11.4 11.4 0 003.6.57 1 1 0 011 1V20a1 1 0 01-1 1A17 17 0 013 4a1 1 0 011-1h3.5a1 1 0 011 1c0 1.25.2 2.45.57 3.57a1 1 0 01-.25 1z" fill="var(--ink)"/></svg>555-014-2288</li>
        <li><svg viewBox="0 0 24 24"><path d="M12 2a7 7 0 00-7 7c0 5.2 7 13 7 13s7-7.8 7-13a7 7 0 00-7-7zm0 9.5A2.5 2.5 0 1112 6.5a2.5 2.5 0 010 5z" fill="var(--ink)"/></svg>17 Harbor Lane suite 40<br>Easton MA 02 xx5</li>
        <li><svg viewBox="0 0 24 24"><circle cx="12" cy="12" r="9" fill="none" stroke="var(--ink)" stroke-width="2"/><path d="M3 12h18M12 3c3 3 3 15 0 18M12 3c-3 3-3 15 0 18" fill="none" stroke="var(--ink)" stroke-width="1.6"/></svg>www.brightharborclinic.com</li>
      </ul>
    </div>
  </div>
</section>

<!-- Outside spread -->
<section class="spread spread--outside">
  <div class="panel">
    <div class="content" style="top:24px;left:16px">
      <h2 class="meet-title">Meet us</h2>
    </div>
    <article class="doctor" style="top:50px">
      <h3>Lena Farrow, DMD, MS</h3>
      <div class="bio-row">
        <p>Dr. Lena Farrow graduated with honors from dental school and completed specialty training in orthodontics with a master's degree. She is board certified and loves helping young patients feel confident about their smile. She is an active member of several professional dental societies and an honor fraternity.</p>
        <div class="portrait" role="img" aria-label="Portrait photo of Dr. Lena Farrow"></div>
      </div>
    </article>
    <article class="doctor" style="top:190px">
      <h3>Peter J. Whitman, DMD</h3>
      <div class="bio-row">
        <div class="portrait" role="img" aria-label="Portrait photo of Dr. Peter J. Whitman"></div>
        <p>Dr. Peter Whitman is board certified in pediatric dentistry and orthodontics. He completed his specialty training at a children's hospital and a university program, and later led a department of orthodontics and pediatric dentistry for many years.</p>
      </div>
    </article>
    <article class="doctor" style="top:320px">
      <h3>Dr. Nora Selim, DMD</h3>
      <div class="bio-row">
        <p>Dr. Nora Selim earned her DMD and completed advanced general practice training. She is an enthusiastic, caring dentist with a passion for improving quality of life. In her spare time she enjoys oil painting and family time.</p>
        <div class="portrait" role="img" aria-label="Portrait photo of Dr. Nora Selim"></div>
      </div>
    </article>
    <svg class="band band--bottom" viewBox="0 0 229 90" height="90">
      <path d="M0 20Q110 70 229 0V10Q120 76 0 30Z" fill="var(--blue-light)"/>
      <path d="M0 38Q120 84 229 18V90H0Z" fill="var(--blue)"/>
    </svg>
  </div>

  <div class="panel panel--shaded">
    <h2 class="reviews-title">REVIEWS</h2>
  </div>

  <div class="panel">
    <div class="cover-top">
      <p class="call">Call us now</p>
      <p class="phone">555-014-2288</p>
      <span class="brand"><span class="mark"></span>Bright Harbor<br>Clinic</span>
    </div>
    <svg class="band band--top" viewBox="0 0 229 130" height="130" style="top:0">
      <path d="M0 110Q110 84 229 98" fill="none" stroke="var(--blue-light)" stroke-width="3"/>
    </svg>
    <svg class="cover-photo" viewBox="0 0 269 270" role="img" aria-label="Photo of a smiling young woman having her teeth shade-checked at the dentist">
      <defs>
        <radialGradient id="photoTone" cx="50%" cy="40%" r="65%">
          <stop offset="0" stop-color="#e6cdbf"/>
          <stop offset=".6" stop-color="#c7a48f"/>
          <stop offset="1" stop-color="#9fb6c6"/>
        </radialGradient>
      </defs>
      <path d="M20 10Q140 -6 249 12V150Q140 250 20 150Z" fill="url(#photoTone)"/>
      <path d="M20 150Q140 250 249 150V180Q140 270 20 190Z" fill="var(--grey)"/>
    </svg>
    <svg class="band band--bottom" viewBox="0 0 229 240" height="240">
      <path d="M0 36Q140 30 229 0V10Q140 42 0 46Z" fill="var(--blue-light)"/>
      <path d="M0 52Q140 48 229 14V240H0Z" fill="var(--blue)"/>
    </svg>
    <div class="offers">
      <h2>Special offers:</h2>
      <p>$69 New patients special<br>$99 Zn-office teeth<br>whiteneeing<br>25%-40% off on Znoisating</p>
    </div>
  </div>
</section>

</body>
</html>
```